Post Sale Flyer For real estate sales in Switzerland

HausPilot is a real estate agent from Switzerland. Thanks to an innovative mix of digitization and personal contact, HausPilot brings sellers and qualified buyers together. You will be accompanied from the free evaluation, the first personal consultation, through professional marketing to the handing over of the keys. Payment only upon successful sale of the property. More information is available on our website: https://www.hauspilot-example.ch/
Goal:
We would like to set up a post-sale flyer that we can distribute to property owners in the region after the sale of a property in the canton of Aargau (Switzerland).
The aim of this should be to arouse the interest of other property owners in the region in selling their property through HausPilot.
The message of the flyer should be: We still have interested parties from the previous sale of the property and can sell more property.
Example: We are selling a property at Lindenweg 14 in Aarau. During the sales process, through our marketing activities, we generate various prospective buyers who are interested in this property. However, we can only sell the property to one buyer. The other interested parties get nothing in a first step. Now we want to use the flyer to make real estate owners in the Aarau region aware that we are already in contact with potential buyers of a property in Aarau and that a sale could be interesting.
The call to action should be for property owners to contact our sales team / Head of Sales Lukas Brenner (telephone number 041 287 15 63): https://www.hauspilot-example.ch/hauspilot/
It would be an advantage to include our Rateo rating (4.7) for customer satisfaction on the flyer as well as our advantages/USPs.
Basically, the design of the flyer is relatively free as long as it fits our corporate identity and our website https://www.hauspilot-example.ch/ and serves the purpose of the flyer. Images can also be chosen freely, although something with real estate and possibly the canton of Aargau (to convey regionality) would certainly be an advantage.
Text can also be freely chosen as long as it serves the purpose of the flyer. For example, it could be as follows:
In the last 12 months we were able to sell x* properties in the canton of Aargau in a short time and had contact with x prospective buyers. Thanks to regional expertise, we broker your property to buyers whose creditworthiness has already been checked, at the best price. Get in contact with us now.
*We would provide the exact figures for finalization as soon as the flyer was accepted internally.
The final flyer design should look modern and appealing, so property owners will contact us.
Target Market(s)
Switzerland
Industry/Entity Type
Immobilien
Requirements
Must have
- Please text in German

```html
<!DOCTYPE html>
<html lang="de">
<head>
<meta charset="utf-8">
<title>HausPilot – Kaufinteressenten für Ihre Immobilie</title>
<link rel="stylesheet" href="https://fonts.googleapis.com/css2?family=Montserrat:wght@500;600;700;800&family=Open+Sans:wght@400;600;700&display=swap">
<style>
:root{
  --navy:#1d3566;
  --blue:#3b73c4;
  --blue-mid:#5b8fd6;
  --blue-light:#b9d3f1;
  --blue-pale:#e6eff9;
  --ink:#2a3346;
  --grey:#6b7486;
  --white:#ffffff;
  --star:#f5b50a;
}
*{margin:0;padding:0;box-sizing:border-box}
html,body{width:849px;height:1200px;overflow:hidden;background:var(--white)}
body{font-family:"Open Sans",Arial,sans-serif;color:var(--ink)}
.flyer{position:relative;width:849px;height:1200px;overflow:hidden;background:var(--white)}

.brand{position:absolute;top:22px;left:38px;display:flex;align-items:center;gap:10px;z-index:5}
.brand-mark{width:26px;height:26px;background:var(--blue);border-radius:4px}
.brand-name{font-family:"Montserrat",sans-serif;font-weight:700;font-size:28px;color:var(--navy)}

.hero-photo{position:absolute;top:0;left:0;width:849px;height:580px;
  background:linear-gradient(180deg,#f4f6f9 0%,#dfe5ec 38%,#c9d2dc 62%,#a9b39a 86%,#8f9b7e 100%)}
.hero-shapes{position:absolute;top:380px;left:0;width:849px;height:230px;z-index:2}
.keys-photo{position:absolute;top:395px;left:30px;width:170px;height:170px;border-radius:50%;
  border:6px solid var(--white);background:radial-gradient(circle at 45% 40%,#e9dcc0 0%,#c8b48c 45%,#8c8f98 100%);z-index:3}

.rating{position:absolute;top:400px;left:598px;width:200px;padding:12px 16px;background:var(--white);
  border-radius:8px;box-shadow:0 4px 14px rgba(0,0,0,.15);display:flex;align-items:center;gap:12px;z-index:3}
.rating-mark{width:34px;height:34px;border-radius:50%;background:var(--blue)}
.rating-score{font-family:"Montserrat",sans-serif;font-weight:700;font-size:15px;color:var(--ink)}
.rating-score .stars{color:var(--star);letter-spacing:1px}
.rating-label{font-weight:700;font-size:16px;color:var(--ink)}

.headline{position:absolute;top:598px;left:55px;width:560px;font-family:"Montserrat",sans-serif;
  font-weight:800;font-size:40px;line-height:1.08;color:var(--navy);text-transform:uppercase;z-index:3}
.intro{position:absolute;top:748px;left:55px;width:500px;font-size:15px;line-height:1.45;color:var(--ink)}

.steps{position:absolute;top:662px;left:585px;width:240px;list-style:none}
.steps li{display:flex;align-items:center;gap:16px;height:62px}
.steps svg{flex:0 0 46px;width:46px;height:46px}
.steps span{font-size:15px;line-height:1.25;color:var(--navy)}

.benefits-title{position:absolute;top:862px;left:55px;font-family:"Montserrat",sans-serif;font-weight:700;font-size:17px;color:var(--navy)}
.benefits{position:absolute;top:898px;left:40px;width:500px;display:flex;list-style:none}
.benefits li{width:125px;text-align:center;padding:0 6px}
.benefits svg{width:56px;height:56px;display:block;margin:0 auto 8px}
.benefits h3{font-size:13px;font-weight:700;line-height:1.2;color:var(--navy);margin-bottom:5px}
.benefits p{font-size:9px;line-height:1.3;color:var(--grey)}

.contact{position:absolute;top:868px;left:560px;width:265px;height:185px;border-radius:10px;
  background:linear-gradient(160deg,var(--blue-mid),var(--blue));color:var(--white);padding:16px 18px}
.contact-title{font-family:"Montserrat",sans-serif;font-weight:700;font-size:17px;line-height:1.2;text-align:center}
.contact-person{display:flex;align-items:center;gap:12px;margin-top:14px}
.contact-photo{width:64px;height:64px;border-radius:50%;border:3px solid var(--white);background:linear-gradient(180deg,#8aa4c8,#3a4e70)}
.contact-name{font-family:"Montserrat",sans-serif;font-weight:700;font-size:18px}
.contact-role{font-size:14px}
.contact-phone{display:flex;align-items:center;gap:10px;margin:12px 0 0 60px;background:var(--white);
  color:var(--navy);border-radius:20px;padding:5px 14px;font-weight:700;font-size:17px;width:max-content}
.contact-phone svg{width:20px;height:20px}

.valuation{position:absolute;top:1064px;left:55px;font-family:"Montserrat",sans-serif;font-weight:700;font-size:15px;color:var(--navy)}

.footer-band{position:absolute;bottom:0;left:0;width:849px;height:120px}
.social{position:absolute;bottom:50px;left:425px;display:flex;gap:12px}
.social span{width:30px;height:30px;border-radius:50%;background:var(--navy)}
.web{position:absolute;bottom:54px;left:600px;display:flex;align-items:center;gap:8px;font-size:14px;color:var(--navy);font-weight:600}
.web svg{width:22px;height:22px}
</style>
</head>
<body>
<main class="flyer">
  <header class="brand"><span class="brand-mark"></span><span class="brand-name">HausPilot</span></header>

  <div class="hero-photo" role="img" aria-label="Foto: modernes weisses Einfamilienhaus, davor eine Familie mit Kindern im Garten"></div>

  <svg class="hero-shapes" viewBox="0 0 849 230" preserveAspectRatio="none" aria-hidden="true">
    <path d="M0 150 C250 120 520 150 849 100 L849 230 L0 230 Z" fill="var(--blue-light)" opacity=".7"/>
    <path d="M0 40 L330 175 C280 190 150 200 0 205 Z" fill="var(--navy)"/>
    <path d="M0 190 C260 175 560 185 849 140 L849 230 L0 230 Z" fill="var(--white)"/>
  </svg>

  <div class="keys-photo" role="img" aria-label="Foto: Hand übergibt Hausschlüssel"></div>

  <div class="rating">
    <span class="rating-mark"></span>
    <div>
      <div class="rating-score">4.7 <span class="stars">★★★★★</span></div>
      <div class="rating-label">Rateo reviews</div>
    </div>
  </div>

  <h1 class="headline">Wir haben noch Kaufinteressenten für Ihre Immobilie</h1>

  <p class="intro">In den letzten 12 Monaten konnten wir in kurzer Zeit x* Liegenschaften im Kanton Aargau verkaufen und hatten Kontakt zu x Kaufinteressenten. Dank regionaler Expertise vermitteln wir Ihre Immobilie zum besten Preis an bereits bonitätsgeprüfte Käufer. Nehmen Sie jetzt Kontakt mit uns auf.</p>

  <ul class="steps">
    <li>
      <svg viewBox="0 0 46 46" fill="none" stroke="var(--blue)" stroke-width="2"><rect x="10" y="6" width="26" height="34" rx="3"/><path d="M16 16h14M16 23h14M16 30h8"/></svg>
      <span>Kostenlose<br>Bewertung</span>
    </li>
    <li>
      <svg viewBox="0 0 46 46" fill="none" stroke="var(--blue)" stroke-width="2"><circle cx="16" cy="16" r="6"/><circle cx="31" cy="16" r="6"/><path d="M5 38c0-7 5-12 11-12s11 5 11 12M20 38c0-7 5-12 11-12s10 5 10 12"/></svg>
      <span>Persönliches<br>Kennenlernen</span>
    </li>
    <li>
      <svg viewBox="0 0 46 46" fill="none" stroke="var(--blue)" stroke-width="2"><path d="M6 22 23 8l17 14M11 18v20h24V18"/><rect x="19" y="27" width="8" height="11"/></svg>
      <span>Wir verkaufen<br>Ihre Immobilie</span>
    </li>
  </ul>

  <h2 class="benefits-title">Ihre Vorteile mit HausPilot</h2>
  <ul class="benefits">
    <li>
      <svg viewBox="0 0 56 56"><circle cx="28" cy="28" r="27" fill="var(--blue-pale)"/><circle cx="28" cy="22" r="7" fill="none" stroke="var(--blue)" stroke-width="2"/><path d="M16 41c0-7 5-11 12-11s12 4 12 11" fill="none" stroke="var(--blue)" stroke-width="2"/></svg>
      <h3>Persönlich und von A–Z</h3>
      <p>Professioneller Service vom ersten Gespräch bis zur Übergabe</p>
    </li>
    <li>
      <svg viewBox="0 0 56 56"><circle cx="28" cy="28" r="27" fill="var(--blue-pale)"/><path d="M16 40V32M24 40V27M32 40V22M40 40V16" stroke="var(--blue)" stroke-width="3"/><path d="M15 24 26 15l6 4 9-8" fill="none" stroke="var(--navy)" stroke-width="2"/></svg>
      <h3>Maximaler Verkaufspreis</h3>
      <p>Bester Preis dank regionaler Expertise, Transparenz und Erfahrung</p>
    </li>
    <li>
      <svg viewBox="0 0 56 56"><circle cx="28" cy="28" r="27" fill="var(--blue-pale)"/><circle cx="28" cy="28" r="12" fill="none" stroke="var(--blue)" stroke-width="2"/><path d="M22 28l4 4 8-8" fill="none" stroke="var(--navy)" stroke-width="2.5"/></svg>
      <h3>Zahlung nur bei Erfolg</h3>
      <p>Immobilienverkauf ohne Risiko, keine versteckten Kosten</p>
    </li>
    <li>
      <svg viewBox="0 0 56 56"><circle cx="28" cy="28" r="27" fill="var(--blue-pale)"/><path d="M28 14l4 9 9 1-7 6 2 9-8-5-8 5 2-9-7-6 9-1z" fill="none" stroke="var(--blue)" stroke-width="2"/></svg>
      <h3>Zufriedene Kunden</h3>
      <p>Gute Kundenbewertungen 4.7 von 5 Sternen bei Rateo</p>
    </li>
  </ul>

  <aside class="contact">
    <p class="contact-title">Nehmen Sie jetzt Kontakt<br>mit uns auf</p>
    <div class="contact-person">
      <div class="contact-photo" role="img" aria-label="Porträtfoto von Lukas Brenner"></div>
      <div>
        <div class="contact-name">Lukas Brenner</div>
        <div class="contact-role">Head of Sales</div>
      </div>
    </div>
    <div class="contact-phone">
      <svg viewBox="0 0 24 24"><path d="M6.6 10.8a15 15 0 0 0 6.6 6.6l2.2-2.2c.3-.3.7-.4 1-.2 1.1.4 2.3.6 3.6.6.6 0 1 .4 1 1V20c0 .6-.4 1-1 1A17 17 0 0 1 3 4c0-.6.4-1 1-1h3.5c.6 0 1 .4 1 1 0 1.3.2 2.5.6 3.6.1.3 0 .7-.2 1z" fill="var(--blue)"/></svg>
      041 287 15 63
    </div>
  </aside>

  <p class="valuation">Jetzt Immobilie kostenlos bewerten</p>

  <svg class="footer-band" viewBox="0 0 849 120" preserveAspectRatio="none" aria-hidden="true">
    <path d="M0 40 C250 90 560 20 849 55 L849 120 L0 120 Z" fill="var(--blue-pale)"/>
    <path d="M0 95 C300 75 600 110 849 85 L849 120 L0 120 Z" fill="var(--blue-light)"/>
  </svg>
  <div class="social" aria-hidden="true"><span></span><span></span><span></span><span></span></div>
  <div class="web">
    <svg viewBox="0 0 24 24" fill="none" stroke="var(--navy)" stroke-width="1.6"><circle cx="12" cy="12" r="9"/><path d="M3 12h18M12 3c3 3 3 15 0 18M12 3c-3 3-3 15 0 18"/></svg>
    https://www.hauspilot-example.ch/hauspilot/
  </div>
</main>
</body>
</html>
```